Business Cards for an 'affordable luxury' inner city home builder in Calgary.

We need a business card design that emulates the progressive, innovative, culture of our company and the modern style of our homes. Use our website www.velmarcrest-ab.com as a reference for the product we build.

Our company builds homes in the inner city space of Calgary, Alberta. We build affordable luxury.

Target Market(s)

Young professional Families

Contact Information for Business Card

Try to maintain consistency with the logo font and the card font.

Requirements
Must have
• The details must include: Name, education, title, phone number, website and email (Address is not as important)
• The design must be uniques (like our logo), elegant, sophisticated and modern.

```html
<!DOCTYPE html>
<html lang="en">
<head>
<meta charset="utf-8">
<title>Velmarcrest Homes Ltd – Business Cards</title>
<link rel="stylesheet" href="https://fonts.googleapis.com/css2?family=Montserrat:wght@500;600;700&family=Open+Sans:wght@400&display=swap">
<style>
  :root {
    --backdrop: #2b2b2b;
    --card: #1f1f1f;
    --card-edge: #f2f2f2;
    --white: #ffffff;
    --silver-light: #b9b9b9;
    --silver-dark: #6a6a6a;
    --detail: #e8e8e8;
  }
  * { margin: 0; padding: 0; box-sizing: border-box; }
  html, body {
    width: 1200px; height: 900px; overflow: hidden;
    background: var(--backdrop);
  }
  .canvas {
    position: relative; width: 1200px; height: 900px;
    background: radial-gradient(ellipse at 60% 40%, #3a3a3a 0%, var(--backdrop) 70%);
  }
  .card {
    position: absolute; left: 250px; width: 700px; height: 400px;
    background: var(--card);
    border-bottom: 6px solid var(--card-edge);
    box-shadow: 0 14px 30px rgba(0,0,0,0.45);
    overflow: hidden;
  }
  .card--front { top: 40px; }
  .card--back { top: 465px; }

  /* front */
  .front-brand {
    position: absolute; left: 150px; top: 130px;
    display: flex; align-items: center; gap: 70px;
  }
  .brand-square {
    width: 90px; height: 90px;
    border: 4px solid #0d0d0d;
  }
  .front-name {
    font-family: 'Montserrat', sans-serif; font-weight: 500;
    font-size: 38px; line-height: 38px; letter-spacing: 2px;
    text-transform: uppercase;
    background: linear-gradient(90deg, var(--silver-dark), var(--silver-light));
    -webkit-background-clip: text; background-clip: text; color: transparent;
  }

  /* back */
  .back-name {
    position: absolute; left: 48px; top: 40px;
    font-family: 'Montserrat', sans-serif; font-weight: 600;
    font-size: 32px; line-height: 32px; letter-spacing: 2px;
    text-transform: uppercase; color: var(--white);
  }
  .contact {
    position: absolute; left: 48px; top: 205px;
    font-family: 'Open Sans', sans-serif; color: var(--detail);
  }
  .contact__person {
    font-family: 'Montserrat', sans-serif; font-weight: 700;
    font-size: 24px; letter-spacing: 1px; text-transform: uppercase;
    color: var(--white); margin-left: 30px;
  }
  .contact__role { font-size: 17px; line-height: 24px; margin-left: 30px; letter-spacing: 0.5px; }
  .contact__list { list-style: none; margin-top: 12px; }
  .contact__item {
    display: flex; align-items: center; gap: 12px;
    font-size: 18px; line-height: 29px; letter-spacing: 0.8px;
  }
  .contact__icon { width: 18px; height: 18px; flex: none; }
  .back-mark {
    position: absolute; right: 80px; top: 120px;
    width: 230px; height: 230px;
    border: 10px solid;
    border-image: linear-gradient(135deg, #111111, #8a8a8a) 1;
  }
</style>
</head>
<body>
<main class="canvas">
  <section class="card card--front">
    <div class="front-brand">
      <div class="brand-square"></div>
      <h1 class="front-name">Velmarcrest<br>Homes<br>Ltd</h1>
    </div>
  </section>

  <section class="card card--back">
    <h2 class="back-name">Velmarcrest<br>Homes<br>Ltd</h2>
    <div class="contact">
      <p class="contact__person">Adrian Kessler</p>
      <p class="contact__role">M.Sc. in Architecture</p>
      <p class="contact__role">Founder &amp; CEO</p>
      <ul class="contact__list">
        <li class="contact__item">
          <svg class="contact__icon" viewBox="0 0 18 18" fill="none" stroke="#e8e8e8" stroke-width="1.6"><rect x="4.5" y="1" width="9" height="16" rx="1.5"/><line x1="8" y1="14.5" x2="10" y2="14.5"/></svg>
          403-555-0148
        </li>
        <li class="contact__item">
          <svg class="contact__icon" viewBox="0 0 18 18" fill="#e8e8e8"><path d="M1 4h16v10H1z"/><path d="M1 4l8 6 8-6" fill="none" stroke="#1f1f1f" stroke-width="1.4"/></svg>
          projects@velmarcrest-ab.com
        </li>
        <li class="contact__item">
          <svg class="contact__icon" viewBox="0 0 18 18" fill="none" stroke="#e8e8e8" stroke-width="1.8"><circle cx="10.5" cy="7.5" r="5.5"/><line x1="6.5" y1="11.5" x2="1.5" y2="16.5"/></svg>
          www.velmarcrest-ab.com
        </li>
      </ul>
    </div>
    <div class="back-mark"></div>
  </section>
</main>
</body>
</html>
```